law firm business cards

I need a business card using my existing logo. Two sided is best because there is a lot of information that needs to go on the card. Use the same general color scheme as logo, but I need one set with the blue background of my website (www.halvorsenlawgrp.com), and one set with white background (to see which one I like best).

Information that must be on there:
Trevor J. Halvorsen
Board Certified Civil Trial Specialist
738 Brinkley Ave., Suite 640
Raleigh, NC 27601

T 919-555-0143
F 919-555-0176

www.halvorsenlawgrp.com
trevor@halvorsenlawgrp.com

Personal Injury | Criminal Law (to separate the two, pls use a bullet point or pipeline symbol "|"

If there is a way to work in the CPRS logo (maybe at the bottom somewhere), put it in, but don't let it detract from the main logo too much.

Also, if there is a way to work it in, put in somewhere: Former Insurance Company Attorney | Former Criminal Prosecutor (to separate the two, pls use a bullet point or pipeline symbol "|"

```html
<!DOCTYPE html>
<html lang="en">
<head>
<meta charset="utf-8">
<title>Halvorsen Law – Business Cards</title>
<link rel="stylesheet" href="https://fonts.googleapis.com/css2?family=Cinzel:wght@500;600&family=Arimo:wght@400&display=swap">
<style>
  :root {
    --navy: #1f3461;
    --navy-text: #23396b;
    --red: #d3223b;
    --sky: #3b7cc9;
    --paper: #ffffff;
    --stage: #e8e8e8;
  }
  * { margin: 0; padding: 0; box-sizing: border-box; }
  html, body { width: 1200px; height: 800px; overflow: hidden; }
  body { background: var(--stage); position: relative; }

  .card {
    position: absolute;
    width: 540px;
    height: 310px;
    overflow: hidden;
    box-shadow: 0 4px 14px rgba(0,0,0,0.18);
  }
  .card--front { left: 50px; top: 150px; background: var(--navy); color: var(--paper); }
  .card--back  { left: 610px; top: 340px; background: var(--paper); color: var(--navy-text); }

  .card__band { position: absolute; left: 0; right: 0; bottom: 0; height: 11px; }
  .card--front .card__band { background: var(--red); }
  .card--back .card__band { background: var(--sky); }

  .brand {
    display: flex;
    align-items: center;
    gap: 10px;
    font-family: 'Cinzel', serif;
    font-weight: 600;
    letter-spacing: 0.5px;
  }
  .brand__mark { display: block; border-radius: 50%; flex: none; }
  .card--front .brand { position: absolute; left: 40px; top: 30px; font-size: 31px; color: var(--paper); }
  .card--front .brand__mark { width: 34px; height: 34px; background: var(--paper); }
  .card--back .brand { justify-content: center; margin-top: 32px; font-size: 22px; color: var(--navy-text); }
  .card--back .brand__mark { width: 24px; height: 24px; background: var(--navy-text); }

  .holder { position: absolute; left: 40px; right: 20px; top: 112px; }
  .holder__name {
    font-family: 'Cinzel', serif;
    font-weight: 500;
    font-size: 29px;
    letter-spacing: 1px;
    line-height: 1.1;
  }
  .holder__title {
    font-family: 'Arimo', sans-serif;
    font-size: 15.5px;
    letter-spacing: 1.6px;
    text-transform: uppercase;
    margin-top: 3px;
  }
  .contact {
    position: absolute; left: 40px; right: 20px; top: 196px;
    font-family: 'Arimo', sans-serif;
    font-size: 13.5px;
    letter-spacing: 0.6px;
    line-height: 1.55;
  }

  .practice {
    text-align: center;
    font-family: 'Cinzel', serif;
    font-weight: 500;
    font-size: 27px;
    letter-spacing: 0.5px;
    margin-top: 26px;
  }
  .credentials {
    text-align: center;
    font-family: 'Arimo', sans-serif;
    font-size: 14px;
    letter-spacing: 1.4px;
    text-transform: uppercase;
    line-height: 1.35;
    margin-top: 10px;
  }
  .seal { display: block; margin: 20px auto 0; }
</style>
</head>
<body>

  <section class="card card--front" aria-label="Business card, blue side">
    <div class="brand"><span class="brand__mark"></span><span class="brand__name">Halvorsen Law</span></div>
    <div class="holder">
      <h1 class="holder__name">Trevor J. Halvorsen</h1>
      <p class="holder__title">Board Certified Civil Trial Specialist</p>
    </div>
    <div class="contact">
      <p>738 Brinkley Ave., Suite 640, Raleigh, NC 27601</p>
      <p>Tel: 919-555-0143 · Fax: 919-555-0176</p>
      <p>www.halvorsenlawgrp.com · trevor@halvorsenlawgrp.com</p>
    </div>
    <div class="card__band"></div>
  </section>

  <section class="card card--back" aria-label="Business card, white side">
    <div class="brand"><span class="brand__mark"></span><span class="brand__name">Halvorsen Law</span></div>
    <h2 class="practice">Personal Injury · Criminal Law</h2>
    <p class="credentials">Former Insurance Company Attorney<br>Former Criminal Prosecutor</p>
    <svg class="seal" width="44" height="44" viewBox="0 0 44 44" role="img" aria-label="Certification board seal">
      <circle cx="22" cy="22" r="20" fill="none" stroke="var(--navy-text)" stroke-width="1.5"/>
      <circle cx="22" cy="22" r="14" fill="none" stroke="var(--navy-text)" stroke-width="1"/>
    </svg>
    <div class="card__band"></div>
  </section>

</body>
</html>
```